Local price comparison site needs a new design

We need new, prettier and especially more efficient, design for local (Slovak Republic) price comparison site. The old one (www.lumivrax.sk) is kind of ugly, but more importantly, it doesn't work for consumer audience (performance indicators are kind of bad). We've started something already, but we're just a bunch of amateurs in this area.

Our first attempt is in the attached file. Colors are such because of the logo (which is dark blue and the only given thing at the moment). The design is a combination and inspired by two other similar sites here:
www.dobrinka.sk
www.kolmabit.cz

We tried, but we're not designers...

Industry/Entity Type

Consumer

Colors

Designer to choose colors to be used in the design.

Requirements
Must have
• Efficient design from performance perspective (we want people to click a lot, content will be attractive enough, we don't want the design to be in the way, but support this)
Vertical banners stripe on the (right) side (see both old and our attempt at new design)
We will need several pages designed (main, category page, product page, search page), but I am not sure how to indicate this in the parameters of the project details
Nice to have
• Please make it simple and easy to read for consumers
Visual design with big pictures

```html
<!DOCTYPE html>
<html lang="sk">
<head>
<meta charset="utf-8">
<title>Lumivrax – porovnanie cien</title>
<link rel="stylesheet" href="https://fonts.googleapis.com/css2?family=Arimo:wght@400;700&display=swap">
<style>
:root{
  --navy:#0c1a8f;
  --link:#1a2aa6;
  --orange:#f39b1b;
  --text:#222;
  --muted:#8a8a8a;
  --line:#d9d9d9;
  --footer:#3a3a3a;
  --footer-text:#6f6f6f;
  --footer-head:#5c5c5c;
}
*{box-sizing:border-box;margin:0;padding:0}
html,body{width:809px;height:1200px;overflow:hidden;background:#fff}
body{position:relative;font-family:"Arimo",Arial,sans-serif;color:var(--text);font-size:9px}
.abs{position:absolute}
.brand{font-weight:700;color:var(--navy);font-size:22px;letter-spacing:-.3px;display:flex;align-items:center;gap:6px}
.brand i{width:14px;height:14px;border-radius:50%;background:var(--navy);display:inline-block}
.search{left:314px;top:25px;width:237px;height:24px;border:1px solid var(--line);border-right:none;background:#fff}
.btn{height:24px;display:flex;align-items:center;justify-content:center;color:#fff;font-size:10px}
.btn-search{left:551px;top:25px;width:63px;background:var(--navy)}
.btn-login{left:622px;top:24px;width:85px;height:25px;background:var(--orange);border-radius:3px}
.hint{left:315px;top:53px;font-size:7.5px;color:var(--muted)}
.topline{left:0;top:84px;width:809px;height:3px;background:#f0f0f0}
.nav{left:100px;top:99px;width:126px;list-style:none}
.nav li{height:25.2px;border-bottom:2px solid #eee;display:flex;align-items:center;justify-content:space-between;font-size:8.6px}
.nav li::after{content:"";border-left:5px solid #ccc;border-top:3px solid transparent;border-bottom:3px solid transparent}
.slider{left:238px;top:99px;width:460px;height:273px;background:radial-gradient(ellipse at 45% 70%,#cfe4f7 0%,#6ea3d6 35%,#2f6eb0 80%)}
.slider .title{position:absolute;right:12px;top:10px;color:#fff;font-size:25px;font-style:italic;font-family:Georgia,serif}
.dots{position:absolute;right:14px;bottom:12px;display:flex;gap:3px}
.dots span{width:10px;height:10px;border-radius:50%;background:#fff}
.dots span:first-child{background:var(--navy);border:2px solid #fff}
.ad-top{left:707px;top:99px;width:102px;height:314px;background:#2b1612;color:#fff;display:flex;align-items:center;justify-content:center}
.ad-top span{writing-mode:vertical-rl;transform:rotate(180deg);font-size:14px;letter-spacing:3px}
.ad-side{left:707px;top:416px;width:102px;height:313px;background:#e1e1e1;display:flex;align-items:center;justify-content:center;font-size:9px}
.heading{left:238px;top:384px;font-size:14.5px;font-weight:400}
.card{top:414px;width:149px;height:156px;border:1px solid var(--line);background:#fff}
.card h3{position:absolute;left:8px;top:8px;font-size:11px;font-weight:400;color:var(--link)}
.card .pic{position:absolute;top:34px}
.card .shop{position:absolute;right:6px;bottom:4px;font-size:8.5px;display:flex;align-items:center;gap:3px}
.card .overlay{position:absolute;left:0;bottom:0;width:100%;height:46px;background:rgba(40,40,40,.85);color:#fff;font-size:8.3px;padding:5px 4px;line-height:12.5px}
.cats{left:246px;top:583px;display:flex;gap:8px;font-size:8.6px;color:var(--link);align-items:center}
.partners{left:238px;top:608px;width:458px;height:94px;border:1px solid var(--line);display:flex;align-items:center;justify-content:space-around;font-size:15px;font-weight:700;color:#555}
.list{top:711px;width:149px;height:149px;border:1px solid var(--line)}
.list h3{margin:8px 0 0 8px;font-size:11px;font-weight:400;color:var(--link)}
.list ul{list-style:none;margin:8px 0 0 8px;font-size:8.6px;line-height:13.2px}
.list li::before{content:"→ "}
.list .more{position:absolute;left:0;bottom:0;width:100%;height:17px;background:var(--navy);color:#fff;font-size:8.6px;display:flex;align-items:center;justify-content:flex-end;padding-right:6px;gap:3px}
.banner-left{left:238px;top:874px;width:311px;height:152px;background:linear-gradient(90deg,#c9dbe8,#dce9f2);display:flex;flex-direction:column;align-items:flex-end;justify-content:center;padding-right:16px;gap:10px}
.banner-left .bn{font-size:17px;font-weight:700}
.banner-left .bt{font-size:16px;font-weight:700;text-align:center}
.banner-right{left:553px;top:874px;width:145px;height:152px;background:linear-gradient(#fff,#cfeef2);border:1px solid var(--orange)}
.banner-right .bn{position:absolute;right:6px;top:6px;color:#f18a1e;font-size:19px;font-weight:700;text-align:right;line-height:20px}
.banner-right .cta{position:absolute;left:44px;bottom:6px;width:92px;height:16px;background:var(--orange);color:#fff;font-size:8.5px;font-weight:700;display:flex;align-items:center;justify-content:center;border-radius:3px}
.footer{left:0;top:1038px;width:809px;height:138px;background:var(--footer)}
.fcol{position:absolute;top:12px;color:var(--footer-text);font-size:8.5px;line-height:13.9px}
.fcol h4{font-size:14.5px;font-weight:400;color:var(--footer-head);margin-bottom:4px}
.bottom-brand{left:106px;top:1180px;font-size:11px}
.totop{left:658px;top:1178px;width:50px;height:18px;background:#222;color:#fff;font-size:6.5px;display:flex;align-items:center;justify-content:center;gap:2px}
</style>
</head>
<body>
<header>
  <div class="abs brand" style="left:102px;top:28px"><i></i>lumivrax.sk</div>
  <div class="abs search"></div>
  <div class="abs btn btn-search">Hľadaj</div>
  <div class="abs btn btn-login">Prihlásenie</div>
  <div class="abs hint">Napr.: snehová fréza, lyže, bežky, korčule, lyžiarky</div>
  <div class="abs topline"></div>
</header>

<ul class="abs nav">
  <li>TV, DVD, foto</li><li>Mobily a komunikácia</li><li>Počítače a hardware</li><li>Domácnosť</li><li>Auto-moto</li><li>Záhrada</li><li>Šport a fitness</li><li>Audio a mp3</li><li>Koníčky a outdoor</li><li>Deti a mamičky</li><li>Krása a zdravie</li><li>Knihy, filmy a hudba</li><li>Software a hry</li><li>Oblečenie a móda</li><li>Nábytok a doplnky</li><li>Erotika</li><li>Hromadné zľavy</li><li>Zľavy dňa</li><li>Naše súťaže</li>
</ul>

<section class="abs slider" role="img" aria-label="Vianočný banner s trblietavými stromčekmi na modrom pozadí">
  <div class="title">Merry Christmas</div>
  <div class="dots"><span></span><span></span><span></span><span></span><span></span></div>
</section>

<aside class="abs ad-top" role="img" aria-label="Reklama reštaurácie Vorenka"><span>Vorenka Restaurant</span></aside>
<aside class="abs ad-side">Reklamy</aside>

<h2 class="abs heading">Vyskúšajte si porovnanie cien v týchto kategóriách:</h2>

<div class="abs card" style="left:238px">
  <h3>Mobilné telefóny</h3>
  <div class="pic" role="img" aria-label="Fotografia mobilného telefónu" style="left:54px;width:40px;height:76px;background:linear-gradient(#dfe7ee,#6b9cc9);border-radius:5px"></div>
  <div class="overlay">1. Tavro Nexa K7<br>2. Kelvo Prima<br>3. Orbit fón Lite</div>
</div>
<div class="abs card" style="left:393px">
  <h3>Knihy</h3>
  <div class="pic" role="img" aria-label="Obálka knihy" style="left:44px;top:34px;width:61px;height:89px;background:linear-gradient(#1d2f5c,#0d1530)"></div>
  <div class="shop">SHOP NOW <svg width="10" height="9" viewBox="0 0 10 9"><path d="M0 1h2l1.5 5h5L10 2H3" fill="none" stroke="#222" stroke-width="1.3"/><circle cx="4" cy="8" r="1"/><circle cx="8" cy="8" r="1"/></svg></div>
</div>
<div class="abs card" style="left:549px">
  <h3>Fotoaparáty</h3>
  <div class="pic" role="img" aria-label="Fotografia zrkadlovky" style="left:22px;top:40px;width:104px;height:82px;background:radial-gradient(circle at 60% 60%,#777,#1e1e1e 70%);border-radius:8px"></div>
  <div class="shop">SHOP NOW <svg width="10" height="9" viewBox="0 0 10 9"><path d="M0 1h2l1.5 5h5L10 2H3" fill="none" stroke="#222" stroke-width="1.3"/><circle cx="4" cy="8" r="1"/><circle cx="8" cy="8" r="1"/></svg></div>
</div>

<nav class="abs cats">
  <span>Notebooky</span><span>Chladničky</span><span>Trúby</span><span>Práčky</span><span>Kuchynské spotrebiče</span><span>Všetky kategórie</span>
  <svg width="14" height="10" viewBox="0 0 14 10"><path d="M1 1l4 4-4 4M7 1l4 4-4 4" fill="none" stroke="var(--navy)" stroke-width="2"/></svg>
</nav>

<div class="abs partners">
  <span>Dixel</span><span>Kolesovo</span><span>Zelená Lúka</span><span>Belvia</span>
</div>

<div class="abs list" style="left:238px">
  <h3>Najobľúbenejšie produkty</h3>
  <ul><li>Tavro Nexa K7 mini</li><li>Pavlo Tab Maxi 32 GB</li><li>Fotexa R200</li><li>Gardon G410</li><li>Rivo KX90</li><li>Trailix Vega</li><li>Orbit Tab Lux 16GB</li></ul>
  <div class="more">More <svg width="14" height="10" viewBox="0 0 14 10"><path d="M1 1l4 4-4 4M7 1l4 4-4 4" fill="none" stroke="#fff" stroke-width="2"/></svg></div>
</div>
<div class="abs list" style="left:393px">
  <h3>Najhľadanejšie značky</h3>
  <ul><li>Orbit</li><li>Tavro</li><li>Kelvo</li><li>Nuvia</li><li>Hartel</li><li>Lumex</li><li>Fjordy</li></ul>
  <div class="more">More <svg width="14" height="10" viewBox="0 0 14 10"><path d="M1 1l4 4-4 4M7 1l4 4-4 4" fill="none" stroke="#fff" stroke-width="2"/></svg></div>
</div>
<div class="abs list" style="left:549px">
  <h3>Poradňa</h3>
  <ul><li>Zimné pneumatiky</li><li>Tablety</li><li>Mobilné telefóny</li><li>Práčky</li><li>Digitálne fotoaparáty</li><li>LCD televízie</li><li>všetky poradne</li></ul>
  <div class="more">More <svg width="14" height="10" viewBox="0 0 14 10"><path d="M1 1l4 4-4 4M7 1l4 4-4 4" fill="none" stroke="#fff" stroke-width="2"/></svg></div>
</div>

<div class="abs banner-left" role="img" aria-label="Reklama obchodu s hodinkami, fotografia dvoch náramkových hodiniek">
  <div class="bn">TIKOMAT.SK</div>
  <div class="bt">jediný onlineshop<br>ktorý nonstop tiká!</div>
</div>
<div class="abs banner-right" role="img" aria-label="Reklama cestovnej kancelárie">
  <div class="bn">CESTOVNÝ<br>RADCA</div>
  <div class="cta">Vyplniť formulár</div>
</div>

<footer class="abs footer">
  <div class="fcol" style="left:100px"><h4>OCnás</h4>Kto sme<br>Je nás vidieť<br>Na stiahnutie<br>Kontakt<br>Obchodné podmienky<br>Podmienky registrácie</div>
  <div class="fcol" style="left:248px"><h4>Pre obchody</h4>Naše služby<br>Cenník<br>XML feed pre eshopy<br>Pridať/Editovať eshop<br>Ocenenia<br>FAQ pre obchody</div>
  <div class="fcol" style="left:399px"><h4>Pre návštevníkov</h4>Súťaže<br>Darčeky zadarmo<br>Bezpečné nakupovanie<br>Zoznam obchodov<br>Služby a firmy<br>FAQ pre návštevníkov</div>
  <div class="fcol" style="left:563px"><h4>Lumivrax</h4>najväčšia nákupná zóna na internete<br>Copyright 2010-2014.<br>Všetky práva vyhradené.</div>
</footer>
<div class="abs brand bottom-brand"><i style="width:8px;height:8px"></i>lumivrax.sk</div>
<div class="abs totop"><svg width="6" height="9" viewBox="0 0 6 9"><path d="M3 9V1M0 4l3-3 3 3" fill="none" stroke="#fff" stroke-width="1.2"/></svg>Back to Top</div>
</body>
</html>
```